Telmoro Business Card

I already have the conplay logo. I need to develop a professional business card layout

Target Market(s)

Business

Industry/Entity Type

Business

Contact Information for Business Card

Company Name: Telmoro Limited

Font styles to use
Sans Serif

Colors

Designer to choose colors to be used in the design.

Requirements
Must have
• Use current logo
• Need two card size options:
• Small Card: 70mm x 28mm (Landscape)
• Square Card: 65mm x 65mm
Nice to have
• I will need 8-10 files for each name, number and email address (details to follow)

```html
<!DOCTYPE html>
<html lang="en">
<head>
<meta charset="utf-8">
<title>Telmoro Business Card</title>
<link rel="stylesheet" href="https://fonts.googleapis.com/css2?family=Roboto:wght@300;400;500;700;900&display=swap">
<style>
  :root {
    --page-bg: #ece9e4;
    --card-bg: #ffffff;
    --ink: #1b1b1f;
    --stripe-blue: #2a2f8f;
    --accent-green: #79c21c;
    --brand: #2a2f8f;
    --pin-green: #6cc12a;
    --phone-red: #e32b2b;
    --mail-blue: #1f7fd1;
    --card-shadow: 0 10px 28px rgba(60, 45, 25, 0.22);
    --mm: 7px;
  }
  * { box-sizing: border-box; margin: 0; padding: 0; }
  html, body {
    width: 1200px;
    height: 800px;
    overflow: hidden;
    background: var(--page-bg);
    font-family: "Roboto", Arial, sans-serif;
    color: var(--ink);
  }
  .sheet {
    width: 1200px;
    height: 800px;
    display: flex;
    align-items: center;
    justify-content: center;
    gap: 48px;
  }
  .card {
    position: relative;
    background: var(--card-bg);
    box-shadow: var(--card-shadow);
    overflow: hidden;
    flex: none;
  }
  /* Small card: 70mm x 28mm landscape */
  .card-small {
    width: calc(70 * var(--mm));
    height: calc(28 * var(--mm));
  }
  /* Square card: 65mm x 65mm */
  .card-square {
    width: calc(65 * var(--mm));
    height: calc(65 * var(--mm));
    display: flex;
    align-items: center;
    justify-content: center;
  }

  .side-stripe {
    position: absolute;
    left: 0; top: 0; bottom: 0;
    width: 10px;
    background: var(--stripe-blue);
  }
  .name-marker {
    position: absolute;
    left: 10px;
    top: 38px;
    width: 0; height: 0;
    border-top: 7px solid transparent;
    border-bottom: 7px solid transparent;
    border-left: 9px solid var(--accent-green);
  }
  .person {
    position: absolute;
    left: 32px;
    top: 30px;
  }
  .person-name {
    font-weight: 300;
    font-size: 18px;
    line-height: 1.1;
  }
  .person-role {
    font-weight: 700;
    font-size: 10px;
    margin-top: 2px;
  }
  .brand-name {
    font-weight: 900;
    color: var(--brand);
    letter-spacing: 1px;
    line-height: 1;
  }
  .card-small .brand-name {
    position: absolute;
    right: 24px;
    top: 22px;
    font-size: 28px;
  }
  .card-square .brand-name { font-size: 50px; }

  .company {
    position: absolute;
    left: 96px;
    bottom: 16px;
  }
  .company-name {
    font-weight: 700;
    font-size: 12px;
    margin-bottom: 3px;
  }
  .contact-list { list-style: none; }
  .contact-item {
    display: flex;
    align-items: flex-start;
    gap: 6px;
    font-size: 10px;
    line-height: 1.3;
  }
  .contact-icon { width: 9px; height: 11px; flex: none; margin-top: 1px; }
</style>
</head>
<body>
<main class="sheet">
  <section class="card card-small" aria-label="Small business card, 70 by 28 mm">
    <div class="side-stripe"></div>
    <div class="name-marker"></div>
    <div class="brand-name">TELMORO</div>
    <div class="person">
      <p class="person-name">Marlen Okafor</p>
      <p class="person-role">Manager Finance</p>
    </div>
    <div class="company">
      <p class="company-name">Telmoro Limited</p>
      <ul class="contact-list">
        <li class="contact-item">
          <svg class="contact-icon" viewBox="0 0 12 14" aria-hidden="true"><path d="M6 0a4.5 4.5 0 0 0-4.5 4.5C1.5 8 6 13 6 13s4.5-5 4.5-8.5A4.5 4.5 0 0 0 6 0z" fill="var(--pin-green)"/><circle cx="6" cy="4.6" r="1.7" fill="#fff"/></svg>
          <span>22 Maple Row, Kingsford ON<br>Canada K4B2R9</span>
        </li>
        <li class="contact-item">
          <svg class="contact-icon" viewBox="0 0 12 14" aria-hidden="true"><rect x="2.5" y="0.8" width="7" height="12.4" rx="1.2" fill="none" stroke="var(--phone-red)" stroke-width="1.5"/><circle cx="6" cy="11" r="0.8" fill="var(--phone-red)"/></svg>
          <span>(+) 555 210 4386</span>
        </li>
        <li class="contact-item">
          <svg class="contact-icon" viewBox="0 0 12 14" aria-hidden="true"><rect x="0.8" y="3" width="10.4" height="8" fill="none" stroke="var(--mail-blue)" stroke-width="1.4"/><path d="M0.8 3 6 7.5 11.2 3" fill="none" stroke="var(--mail-blue)" stroke-width="1.4"/></svg>
          <span>info@telmoro.com</span>
        </li>
      </ul>
    </div>
  </section>

  <section class="card card-square" aria-label="Square business card, 65 by 65 mm">
    <div class="brand-name">TELMORO</div>
  </section>
</main>
</body>
</html>
```